Tiny Summit Marketing Booklet Design

•To create 2 brochure designs
1st booklet Complex 8.5X11” 20-24 page Brochure booklet targetted at Enterprise clients

2rd booklet 10-12 page Borchure booklet for parents and schools

•Text content, photos and logos to be supplied by customer

We need a product/service brochure that explains our programme “Tiny Summit” managed and run byViva Kids Pte ltd. The designer must clearly outline our vision and mission of this programme

Lumo kids is part of the Lumo Group of Education companies that develop programmes and educational software programme for schools, institutions and its service centers.

Tiny Summit is a Sports and Education programme that is in the business of changing lives through values.
The materials are targeted to be distributed to School Leaders and Parents.

We are looking for a professional look for both brochure booklet with our rebranded logos. The Logos of both the company and the product logo Tiny Summit will be uploaded within the week with further materials to be developed.

For the purposes of this contest and shortlist selection, we require only the 1st 4 pages to be designed.

The corporate colors are Navy Blue and Golden Yellow. Designers are welcome to design creatively with a new look or colours without losing any professionaly look.

Please use the uploaded existing draft in 2 powerpoints to begin your design.

Target Market(s)

School leaders which include Principals and corporate stakeholders

You can view a similar progamme onn TV run by the founder of Tiny Summit at http://clipvault.example/watch/qTrb82Lxm0p

Industry/Entity Type

Software

Requirements
Should not have
• have any playful colours

```html
<!DOCTYPE html>
<html lang="en">
<head>
<meta charset="utf-8">
<title>Tiny Summit Booklet – Pages 1–4</title>
<link href="https://fonts.googleapis.com/css2?family=Poiret+One&family=Dancing+Script:wght@600&family=Cinzel&family=Arimo:wght@400;700&display=swap" rel="stylesheet">
<style>
:root{
  --navy:#1e1d5c;
  --navy-deep:#05051a;
  --navy-mid:#2a3590;
  --gold:#ffc20e;
  --gold-deep:#f39a12;
  --gold-soft:#ffd84a;
  --paper:#ffffff;
  --ink:#111111;
  --frame:#d4d4d4;
  --clip:#c9c9c9;
}
*{margin:0;padding:0;box-sizing:border-box}
html,body{width:848px;height:1200px;overflow:hidden;background:#fff}
.spread{position:relative;width:848px;height:1200px}
.backdrop{position:absolute;left:92px;top:0;width:663px;height:1200px;background:var(--gold)}
.page{position:absolute;width:292px;height:382px;box-shadow:3px 4px 8px rgba(0,0,0,.35);overflow:hidden;font-family:"Arimo",Arial,sans-serif;color:var(--ink)}
.cover{top:6px;height:380px;width:294px;background:linear-gradient(90deg,var(--navy) 0%,var(--navy) 40%,var(--navy-deep) 100%)}
.cover--front{left:121px}
.cover--back{left:426px;background:linear-gradient(90deg,var(--navy-deep) 0%,var(--navy) 60%,var(--navy) 100%)}
.sq{position:absolute}
.sq--gold{background:linear-gradient(135deg,var(--gold-soft),var(--gold-deep))}
.sq--blue{background:linear-gradient(135deg,var(--navy-mid),#243088)}
.title{position:absolute;font-family:"Poiret One",sans-serif;color:var(--gold);font-weight:400;white-space:nowrap;transform-origin:left top;line-height:1}
.title--main{left:15px;top:98px;font-size:44px;letter-spacing:0;transform:scaleX(.74)}
.title--values{left:94px;top:172px;font-size:38px;letter-spacing:0;transform:scaleX(.78)}
.title--with{position:absolute;left:126px;top:145px;font-family:"Dancing Script",cursive;font-size:20px;color:var(--gold-deep);transform:rotate(-14deg);line-height:1}
.brand{position:absolute;left:104px;top:150px;display:flex;align-items:center;gap:5px;font-family:"Arimo",sans-serif;font-weight:700;font-size:13px;color:var(--gold)}
.brand__mark{width:12px;height:12px;background:var(--gold)}
.partner{position:absolute;left:98px;top:202px;font-family:"Cinzel",serif;font-size:8.5px;letter-spacing:1px;color:var(--gold)}
.inner{background:var(--paper)}
.row2{top:403px}.row3{top:804px}
.col1{left:127px}.col2{left:430px}
.frame{position:absolute;inset:0}
.heading{position:absolute;top:90px;left:0;width:100%;text-align:center;font-weight:700;font-size:6.5px}
.folio{position:absolute;top:355px;left:0;width:100%;text-align:center;font-weight:700;font-size:6.5px}
.toc{position:absolute;left:73px;top:119px;list-style:none;font-size:6px}
.toc li{display:flex;align-items:center;gap:6px;height:17.5px}
.toc li::before{content:"";width:6px;height:6px;background:var(--gold)}
.about{position:absolute;left:46px;top:111px;width:200px;font-size:5.6px;line-height:1.35}
.about p{text-indent:10px;margin-bottom:8px}
.team{position:absolute;left:46px;top:110px;width:210px;font-size:5.6px;line-height:1.4}
.team p{margin-bottom:7px}
.team .div{font-weight:700;font-style:italic;text-decoration:underline}
.clipping{position:absolute;background:linear-gradient(160deg,#e2e2e2,var(--clip));border:1px solid #b5b5b5}
.quote{position:absolute;font-size:5.6px;line-height:1.35;text-align:justify}
</style>
</head>
<body>
<div class="spread">
  <div class="backdrop"></div>

  <section class="page cover cover--front">
    <div class="sq sq--gold" style="left:42px;top:193px;width:21px;height:23px"></div>
    <div class="sq sq--blue" style="left:143px;top:254px;width:100px;height:97px"></div>
    <div class="sq sq--gold" style="left:86px;top:208px;width:69px;height:94px"></div>
    <div class="sq sq--blue" style="left:55px;top:239px;width:66px;height:65px"></div>
    <h1 class="title title--main">CHANGING LIVES</h1>
    <span class="title--with">with</span>
    <span class="title title--values">VALUES</span>
  </section>

  <section class="page cover cover--back">
    <div class="brand"><span class="brand__mark"></span>Tiny Summit</div>
    <p class="partner">IN PARTNERSHIP WITH</p>
    <div class="sq sq--gold" style="left:0;top:213px;width:9px;height:9px"></div>
    <div class="sq sq--gold" style="left:17px;top:225px;width:11px;height:11px"></div>
    <div class="sq sq--gold" style="left:32px;top:237px;width:7px;height:7px"></div>
    <div class="sq sq--gold" style="left:40px;top:249px;width:8px;height:8px"></div>
    <div class="sq sq--gold" style="left:52px;top:239px;width:5px;height:5px"></div>
    <div class="sq sq--gold" style="left:35px;top:261px;width:6px;height:6px"></div>
    <div class="sq sq--gold" style="left:55px;top:256px;width:5px;height:5px"></div>
    <div class="sq sq--gold" style="left:67px;top:259px;width:4px;height:4px"></div>
  </section>

  <!-- Page 1 -->
  <section class="page inner row2 col1">
    <svg class="frame" viewBox="0 0 292 382" aria-hidden="true"><g fill="var(--frame)">
      <path d="M22 22 L100 22 Q40 26 30 30 L26 110 Q24 40 22 22Z"/>
      <path d="M270 22 L192 22 Q252 26 262 30 L266 110 Q268 40 270 22Z"/>
      <path d="M22 360 L100 360 Q40 356 30 352 L26 272 Q24 342 22 360Z"/>
      <path d="M270 360 L192 360 Q252 356 262 352 L266 272 Q268 342 270 360Z"/></g></svg>
    <h2 class="heading">INTRODUCTION</h2>
    <ul class="toc"><li>CONTENT PAGE</li><li>ABOUT US</li><li>LEADERSHIP TEAM</li></ul>
    <p class="folio">1</p>
  </section>

  <!-- Page 2 -->
  <section class="page inner row2 col2">
    <svg class="frame" viewBox="0 0 292 382" aria-hidden="true"><g fill="var(--frame)">
      <path d="M22 22 L100 22 Q40 26 30 30 L26 110 Q24 40 22 22Z"/>
      <path d="M270 22 L192 22 Q252 26 262 30 L266 110 Q268 40 270 22Z"/>
      <path d="M22 360 L100 360 Q40 356 30 352 L26 272 Q24 342 22 360Z"/>
      <path d="M270 360 L192 360 Q252 356 262 352 L266 272 Q268 342 270 360Z"/></g></svg>
    <h2 class="heading">ABOUT US</h2>
    <div class="about">
      <p>Lumo Kids Pte Ltd is an Education and Sporting company which has approved SEP and MOE PAL certifications for its sporting programmes.</p>
      <p>Lumo Kids operates commercially as a social enterprise to implement Tiny Summit as an ability driven Sports and Academic development programme targeted at lower primary students.</p>
      <p>It has amongst its management very experienced and distinguished personalities in the Educational sector, from former senior civil servants in MOE to advisors from CTI and the Private Sector.</p>
    </div>
    <p class="folio">2</p>
  </section>

  <!-- Page 3 -->
  <section class="page inner row3 col1">
    <svg class="frame" viewBox="0 0 292 382" aria-hidden="true"><g fill="var(--frame)">
      <path d="M22 22 L100 22 Q40 26 30 30 L26 110 Q24 40 22 22Z"/>
      <path d="M270 22 L192 22 Q252 26 262 30 L266 110 Q268 40 270 22Z"/>
      <path d="M22 360 L100 360 Q40 356 30 352 L26 272 Q24 342 22 360Z"/>
      <path d="M270 360 L192 360 Q252 356 262 352 L266 272 Q268 342 270 360Z"/></g></svg>
    <h2 class="heading">LEADERSHIP TEAM</h2>
    <div class="team">
      <p><b>MD</b> : Mr Aldric Venn</p>
      <p><b>GM</b> : Mr Doran Lisk</p>
      <p class="div">Sports Division</p>
      <p><b>Senior Director</b> : Mr Teo Wen Hale<br><b>Corporate Director</b>: Marissa Kellan Roe</p>
      <p class="div">Education Division: Professional &amp; Curriculum Division</p>
      <p><b>Senior Director</b> : Mr Nolan Petrie<br><b>CTI Consultants</b> : Prof Selma Quill, Prof Ravinder Osei</p>
      <p class="div">Finance Division: Public Accountability and Corporate Governance</p>
      <p><b>Director</b> : Mrs Lena Marsh</p>
      <p><b>Partners</b> : Ms Ivy Calder</p>
    </div>
    <p class="folio">3</p>
  </section>

  <!-- Page 4 -->
  <section class="page inner row3 col2">
    <svg class="frame" viewBox="0 0 292 382" aria-hidden="true"><g fill="var(--frame)">
      <path d="M22 22 L100 22 Q40 26 30 30 L26 110 Q24 40 22 22Z"/>
      <path d="M270 22 L192 22 Q252 26 262 30 L266 110 Q268 40 270 22Z"/>
      <path d="M22 360 L100 360 Q40 356 30 352 L26 272 Q24 342 22 360Z"/>
      <path d="M270 360 L192 360 Q252 356 262 352 L266 272 Q268 342 270 360Z"/></g></svg>
    <h2 class="heading">CURRENT LANDSCAPE / MOE's DIRECTION</h2>
    <div class="clipping" role="img" aria-label="Newspaper clipping on education centring on character-building, with portrait" style="left:35px;top:106px;width:140px;height:77px"></div>
    <p class="quote" style="left:182px;top:110px;width:76px">"Education Minister Lim Arden Shaw stressed the need to focus on personal, moral and citizenship values to prepare Singapore's Young people for profound global changes."</p>
    <div class="clipping" role="img" aria-label="Newspaper clipping on education about skills and character" style="left:132px;top:201px;width:127px;height:147px"></div>
    <p class="quote" style="left:38px;top:224px;width:91px">"Education today is about developing in our students an enduring core of competencies, values and character, so that they have the resilience to survive and succeed in a future which could be very different from the one that we are living today, said Education Minister Lim Arden Shaw"</p>
    <p class="folio">4</p>
  </section>
</div>
</body>
</html>
```